Dental Office Looking for Modern, simple business cards

We just acquired our logo. Now we would like to make business cards. We are a dental office with two doctors. We are husband and wife and have a small boutique dental practice in a small town. We love our patients and they are always asking us to give our business cards to their friends. Please help us make business cards :-)

Target Market(s)

30-60 yr old

Industry/Entity Type

Dental Clinic

Contact Information for Business Card

Birch Hollow Dental P.C.
Family and Cosmetic Dentistry
4827 Dunmore Rd. Schenectady NY 12309
Tel: 518 642 8817 Fax: 518 642 8830

Dr. Tomas K. Elridge DDS
Dr. Marisol Anne Whitby DDS

Font styles to use
Serif
Sans Serif

Requirements
Must have
• Simple clean design, modern, colorful. Should incorporate the logo.
Nice to have
• dental imagery ( teeth, smile, etc ...).

```html
<!DOCTYPE html>
<html lang="en">
<head>
<meta charset="utf-8">
<title>Birch Hollow Dental – Business Cards</title>
<link rel="stylesheet" href="https://fonts.googleapis.com/css2?family=Tinos&family=Alegreya+Sans:wght@400&display=swap">
<style>
  :root {
    --stage: #000000;
    --card-white: #ffffff;
    --brand-blue: #1e73be;
    --ink: #1f1f1f;
    --rule: #555555;
    --faint-front: #eceff7;
    --faint-back: rgba(255,255,255,0.1);
  }
  * { margin: 0; padding: 0; box-sizing: border-box; }
  html, body { width: 900px; height: 1200px; overflow: hidden; background: var(--stage); }
  .canvas { position: relative; width: 900px; height: 1200px; }

  .card {
    position: absolute; left: 80px; width: 734px; height: 430px;
    border-radius: 22px; overflow: hidden;
  }
  .card-front { top: 127px; background: var(--card-white); }
  .card-back { top: 645px; background: var(--brand-blue); }

  .deco-circle {
    position: absolute; border-radius: 50%;
  }
  .card-front .deco-circle { left: 480px; top: 10px; width: 250px; height: 250px; background: var(--faint-front); }
  .card-back .deco-circle { left: 430px; top: 30px; width: 300px; height: 300px; background: var(--faint-back); }

  .brand-name {
    position: absolute; font-family: "Tinos", serif; font-weight: 400;
    letter-spacing: 1px; white-space: nowrap;
  }
  .card-front .brand-name { left: 50px; top: 80px; font-size: 38px; color: var(--brand-blue); }
  .card-back .brand-name { left: 0; width: 100%; text-align: center; top: 168px; font-size: 38px; color: var(--card-white); }

  .tagline {
    position: absolute; font-family: "Alegreya Sans", sans-serif; font-size: 19px; white-space: nowrap;
  }
  .card-front .tagline { left: 107px; top: 160px; color: var(--brand-blue); }
  .card-back .tagline { left: 0; width: 100%; text-align: center; top: 248px; color: var(--card-white); }

  .doctor {
    position: absolute; top: 287px; font-family: "Tinos", serif; font-size: 17.5px; color: var(--ink); white-space: nowrap;
  }
  .doctor .credential { color: var(--brand-blue); }
  .doctor-left { left: 50px; }
  .doctor-right { right: 47px; }

  .divider { position: absolute; left: 50px; right: 47px; top: 321px; height: 1.5px; background: var(--rule); }

  .contact {
    position: absolute; font-family: "Tinos", serif; font-size: 16px; color: var(--ink);
    display: flex; align-items: center; gap: 9px; white-space: nowrap;
  }
  .contact svg { width: 19px; height: 19px; flex: none; }
  .contact-phone { left: 50px; top: 336px; }
  .contact-fax { left: 50px; top: 360px; }
  .contact-address { right: 46px; top: 336px; }

  .footer-band { position: absolute; left: 0; right: 0; bottom: 0; height: 17px; background: var(--brand-blue); }
</style>
</head>
<body>
<main class="canvas">
  <section class="card card-front" aria-label="Business card front">
    <div class="deco-circle" aria-hidden="true"></div>
    <div class="brand-name">BIRCH HOLLOW DENTAL</div>
    <div class="tagline">Family and Cosmetic Dentistry</div>

    <div class="doctor doctor-left">Dr. Tomas K. Elridge <span class="credential">DDS</span></div>
    <div class="doctor doctor-right">Dr. Marisol Anne Whitby <span class="credential">DDS</span></div>
    <div class="divider"></div>

    <div class="contact contact-phone">
      <svg viewBox="0 0 20 20" aria-hidden="true"><circle cx="10" cy="10" r="10" fill="var(--brand-blue)"/><path d="M6.5 5.2c.5-.4 1.1-.3 1.4.2l1 1.6c.2.4.1.9-.2 1.2l-.6.5c.5 1.1 1.4 2 2.5 2.6l.5-.6c.3-.4.8-.4 1.2-.2l1.6 1c.5.3.6 1 .2 1.4l-.7.8c-.6.6-1.5.7-2.3.3-2.4-1.2-4.3-3.1-5.4-5.5-.4-.8-.2-1.7.4-2.3z" fill="#fff"/></svg>
      <span>518 642 8817</span>
    </div>
    <div class="contact contact-fax">
      <svg viewBox="0 0 20 20" aria-hidden="true"><circle cx="10" cy="10" r="10" fill="var(--brand-blue)"/><rect x="7" y="5" width="6" height="3" fill="#fff"/><rect x="5" y="8.5" width="10" height="5" rx="1" fill="#fff"/><rect x="7" y="12" width="6" height="3.5" fill="#fff" stroke="var(--brand-blue)" stroke-width="0.8"/></svg>
      <span>518 642 8830</span>
    </div>
    <div class="contact contact-address">
      <span>4827 Dunmore Rd. Schenectady NY 12309</span>
      <svg viewBox="0 0 20 20" aria-hidden="true"><circle cx="10" cy="10" r="10" fill="var(--brand-blue)"/><path d="M10 4.5a3.8 3.8 0 0 0-3.8 3.8c0 2.8 3.8 7 3.8 7s3.8-4.2 3.8-7A3.8 3.8 0 0 0 10 4.5z" fill="#fff"/><circle cx="10" cy="8.3" r="1.4" fill="var(--brand-blue)"/></svg>
    </div>
    <div class="footer-band"></div>
  </section>

  <section class="card card-back" aria-label="Business card back">
    <div class="deco-circle" aria-hidden="true"></div>
    <div class="brand-name">BIRCH HOLLOW DENTAL</div>
    <div class="tagline">Family and Cosmetic Dentistry</div>
  </section>
</main>
</body>
</html>
```